Massage Therapy and Energy Healing Practice

I am a massage therapist, Reiki energy healer, I sell herbs and oils, and also a health lifestyle coach. I need a design that is strong because I'm not a spa. I do therapeutic work, but I want a touch of the energy and spiritual healing I do as well to be included in the design. I like blue, green, or purple colors. I live in the Blue Ridge Mountains of VA and even though my practice is in the city I like my love for nature and the earth to show through. I would like a single image logo so I can use the image many places. I need a strong brand that will let others know that I combine massage therapy in a therapeutic way while keeping my touches of energy healing, nurturing, herb crafting, and mother earth loving ways.
Updates

Just some things about me:I like to hike. I live on a farm. I own horses, cows, sheep and dogs. I love nature and the energy in produces. I'm very spiritual. I don't know how these things might help or if they do, but I know that my personality might help inspire what I will find good in a design. Added Sunday, December 13, 2015

Target Market(s)

People in pain. People who need spiritual council. Need herbal medicine advice. Holistic healthcare.

Industry/Entity Type

Massage

Contact Information for Business Card

Kneadwell Studio
Lorna T. Whitcombe C.M.T, R.M.T
40519 Hollin Creek Court, Tallowdale, VA
540-718-2437

Colors
3176b5
85abd2
876aae
9bcb3c

Requirements
Must have
• Strong Branding that promotes my massage therapy practice first
Nice to have
• Something to evoke my herbal medicine, my energy healing, my spiritual side

```html
<!DOCTYPE html>
<html lang="en">
<head>
<meta charset="utf-8">
<title>Kneadwell Studio — Business Cards</title>
<link href="https://fonts.googleapis.com/css2?family=Comfortaa:wght@300&family=Open+Sans:wght@400;600&display=swap" rel="stylesheet">
<style>
  :root {
    --bg: #e9e6e1;
    --card-white: #f7f7f6;
    --brand-blue: #3176b5;
    --blue-deep: #2a6aa8;
    --blue-light: #4fa3d4;
    --soft-blue: #85abd2;
    --leaf-green: #9bcb3c;
    --ink-white: #ffffff;
    --shadow: rgba(40, 30, 20, 0.28);
  }
  * { margin: 0; padding: 0; box-sizing: border-box; }
  html, body { width: 1200px; height: 1062px; overflow: hidden; }
  body { background: var(--bg); position: relative; font-family: "Open Sans", sans-serif; }

  .card {
    position: absolute;
    width: 600px;
    height: 343px;
    border-radius: 3px;
    overflow: hidden;
    box-shadow: 0 10px 28px var(--shadow);
  }

  /* Front */
  .card-front { left: 80px; top: 170px; background: var(--card-white); }
  .front-brand {
    position: absolute; left: 0; right: 0; top: 0; height: 200px;
    display: flex; align-items: center; justify-content: center; gap: 14px;
  }
  .brand-dot { width: 22px; height: 22px; border-radius: 50%; background: var(--brand-blue); }
  .brand-name-front {
    font-family: "Comfortaa", sans-serif; font-weight: 300;
    font-size: 40px; color: var(--leaf-green); letter-spacing: 0.5px;
  }
  .front-stripe { position: absolute; left: 0; right: 0; top: 200px; height: 9px; background: var(--leaf-green); }
  .front-band {
    position: absolute; left: 0; right: 0; top: 209px; bottom: 0;
    background: linear-gradient(180deg, var(--blue-light) 0%, var(--brand-blue) 100%);
    color: var(--ink-white);
  }
  .holder { position: absolute; left: 30px; bottom: 26px; }
  .holder-name { font-weight: 600; font-size: 17px; }
  .holder-title { font-size: 12px; opacity: 0.85; margin-top: 2px; }
  .contact { position: absolute; right: 30px; top: 22px; list-style: none; font-size: 12.5px; line-height: 1.55; }
  .contact li { display: flex; gap: 8px; align-items: flex-start; }
  .contact svg { width: 11px; height: 11px; margin-top: 4px; flex: none; fill: var(--ink-white); }
  .contact .addr { display: block; }

  /* Back */
  .card-back {
    left: 520px; top: 580px;
    background: radial-gradient(ellipse at 55% 40%, var(--blue-light) 0%, var(--brand-blue) 60%, var(--blue-deep) 100%);
    display: flex; align-items: center; justify-content: center; gap: 16px;
  }
  .card-back .brand-dot { background: var(--ink-white); width: 26px; height: 26px; }
  .brand-name-back {
    font-family: "Comfortaa", sans-serif; font-weight: 300;
    font-size: 44px; color: var(--ink-white);
  }
</style>
</head>
<body>
  <section class="card card-front" aria-label="Business card front">
    <div class="front-brand">
      <span class="brand-dot"></span>
      <span class="brand-name-front">Kneadwell Studio</span>
    </div>
    <div class="front-stripe"></div>
    <div class="front-band">
      <ul class="contact">
        <li><svg viewBox="0 0 12 12"><path d="M3 1l2 2-1 1.5a6 6 0 0 0 3.5 3.5L9 7l2 2-1.5 2A9 9 0 0 1 1 2.5z"/></svg>540-718-2437</li>
        <li><svg viewBox="0 0 12 12"><circle cx="6" cy="6" r="5" fill="none" stroke="#fff" stroke-width="1.6"/><circle cx="6" cy="6" r="2"/></svg>info@kneadwellstudio.com</li>
        <li><svg viewBox="0 0 12 12"><path d="M6 0a4 4 0 0 1 4 4c0 3-4 8-4 8S2 7 2 4a4 4 0 0 1 4-4z"/></svg><span class="addr">40519 Hollin Creek Court,<br>Tallowdale, VA</span></li>
      </ul>
      <div class="holder">
        <p class="holder-name">Lorna T. Whitcombe</p>
        <p class="holder-title">C.M.T, R.M.T</p>
      </div>
    </div>
  </section>

  <section class="card card-back" aria-label="Business card back">
    <span class="brand-dot"></span>
    <span class="brand-name-back">Kneadwell Studio</span>
  </section>
</body>
</html>
```